Looking for a hot sauce label designed
Name: Copper Lantern Hot sauce
Graphic: dragon in pictures supplied and the flame bigger going out in front of the dragon or happy for you to design a dragon in a similar style
Text font: using the text supplied for the name of the product only
Colour: Black graphic and text on light brown paper
Style: sketch dragon and text - simple minimalistic design
Label size: 7cm height x 17cm width

Target Market(s)

To sell in bars and supermarkets

Font styles to use
Script

Colors

Designer to choose only greyscale colors for use in the design.

Requirements
Must have
• Name of product: Copper Lantern Hot Sauce
Batch No:
Business name and address
Best before date:
Nutrition Information Panel
Ingredients
Shake well before use
Keep refrigerated after opening
Australian made using 100% local ingredients
175ml
Room for a barcode
Nice to have
• Any changes you think will improve label design

```html
<!DOCTYPE html>
<html lang="en">
<head>
<meta charset="utf-8">
<title>Copper Lantern Hot Sauce – Label</title>
<link rel="stylesheet" href="https://fonts.googleapis.com/css2?family=Arimo:wght@400;700&family=Gochi+Hand&display=swap">
<style>
  :root {
    --paper: #ffffff;
    --panel: #e6e6e6;
    --ink: #111111;
    --muted: #c4c4c4;
    --soft-ink: #444444;
    --sketch-light: #eef0f4;
    --sketch-dark: #8a909c;
  }
  * { margin: 0; padding: 0; box-sizing: border-box; }
  html, body { width: 1200px; height: 720px; overflow: hidden; background: var(--paper); }
  body { font-family: "Arimo", Arial, sans-serif; color: var(--ink); }
  .label { position: relative; width: 1200px; height: 720px; background: var(--paper); }

  .panel {
    position: absolute; left: 44px; width: 285px;
    background: var(--panel);
    outline: 4px dashed var(--paper); outline-offset: -3px;
  }
  .nutrition { top: 44px; height: 360px; }
  .nutrition h2 { position: absolute; left: 13px; top: 13px; font-size: 19.5px; font-weight: 700; letter-spacing: 0.2px; }
  .nutrition .meta { position: absolute; left: 14px; font-size: 15.5px; }
  .nutrition .servings { top: 48px; }
  .nutrition .size { top: 75px; }
  .nutrition table { position: absolute; left: 14px; top: 108px; border-collapse: collapse; font-size: 15.5px; }
  .nutrition td, .nutrition th { font-weight: 400; text-align: left; padding: 0; height: 26.6px; vertical-align: top; }
  .nutrition thead th { height: 46px; line-height: 20px; }
  .nutrition .col-name { width: 115px; }
  .nutrition .col-serve { width: 77px; }
  .nutrition .sub { padding-left: 4px; }

  .ingredients { top: 424px; height: 102px; padding: 11px 34px 11px 13px; font-size: 15.4px; line-height: 20px; }
  .ingredients strong { font-weight: 700; }

  .caution { top: 546px; height: 102px; }
  .caution h3 { position: absolute; left: 14px; top: 12px; font-size: 19.5px; font-weight: 700; text-decoration: underline; }
  .caution ul { position: absolute; left: 25px; top: 46px; list-style: none; font-size: 16px; font-weight: 700; line-height: 26px; }

  .dragon-art {
    position: absolute; left: 512px; top: 72px; width: 476px; height: 336px;
    background: radial-gradient(ellipse at 45% 50%, var(--sketch-dark) 0%, #c7cbd3 40%, var(--sketch-light) 70%, var(--paper) 100%);
  }

  .product-name {
    position: absolute; left: 420px; top: 408px; width: 620px; text-align: center;
    font-family: "Gochi Hand", cursive; font-weight: 400; color: var(--ink); line-height: 1;
  }
  .product-name .line-one { display: block; font-size: 86px; }
  .product-name .line-two { display: block; font-size: 80px; margin-top: 6px; }

  .volume { position: absolute; left: 433px; top: 629px; font-size: 16px; }

  .barcode-space {
    position: absolute; left: 984px; top: 548px; width: 108px; height: 72px;
    background: var(--paper); border: 1.5px solid var(--muted);
  }

  .product-notes {
    position: absolute; left: 433px; top: 656px; width: 660px;
    font-size: 12px; line-height: 17px; color: var(--soft-ink);
  }
  .product-notes strong { color: var(--ink); }

  .origin-claim {
    position: absolute; left: 1118px; top: 262px;
    transform-origin: 0 0; transform: rotate(-90deg);
    color: var(--muted); font-weight: 700; font-size: 15px; line-height: 18px; white-space: nowrap; text-align: right; width: 212px;
  }

  .batch { position: absolute; left: 1106px; top: 438px; width: 46px; height: 210px; background: var(--panel); outline: 4px dashed var(--paper); outline-offset: -3px; }
  .batch .write-in { position: absolute; left: 8px; top: 10px; width: 30px; height: 94px; background: var(--paper); border-radius: 8px; }
  .batch .batch-label {
    position: absolute; left: 14px; top: 198px; transform-origin: 0 0; transform: rotate(-90deg);
    color: var(--paper); font-size: 14px; white-space: nowrap;
  }
</style>
</head>
<body>
<main class="label">
  <section class="panel nutrition">
    <h2>NUTRITION INFORMATION</h2>
    <p class="meta servings">Servings per package:&nbsp; 17.00</p>
    <p class="meta size">Serving size:&nbsp; 170.00m</p>
    <table>
      <thead>
        <tr><th class="col-name"></th><th class="col-serve">Ave. per<br>Serve</th><th>Ave. per<br>100ml</th></tr>
      </thead>
      <tbody>
        <tr><td>Energy</td><td>257KJ</td><td>151KJ</td></tr>
        <tr><td>Protein</td><td>1.5g</td><td>0.9g</td></tr>
        <tr><td>Fat, Total</td><td>3.2g</td><td>1.9g</td></tr>
        <tr><td class="sub">-Saturated</td><td>0.5g</td><td>0.3g</td></tr>
        <tr><td>Carbohydrate</td><td>4.3g</td><td>2.5g</td></tr>
        <tr><td class="sub">-Sugars</td><td>3.7g</td><td>2.2g</td></tr>
        <tr><td>Sodium</td><td>262mg</td><td>154mg</td></tr>
      </tbody>
    </table>
  </section>

  <section class="panel ingredients">
    <p><strong>Ingredients:</strong> Carrots, Onion, Habanero, Water, Lime juice, Garlic, White vinegar, Vegetable oil, Ginger, Cilantro, Salt, Pepper.</p>
  </section>

  <section class="panel caution">
    <h3>CAUTION:</h3>
    <ul>
      <li>- Keep out of reach of children.</li>
      <li>- Keep away and out of eyes.</li>
    </ul>
  </section>

  <div class="dragon-art" role="img" aria-label="Pencil sketch of a plump, grinning dragon sitting with wings and long tail, breathing a curl of flame"></div>

  <h1 class="product-name">
    <span class="line-one">Copper Lantern</span>
    <span class="line-two">Hot Sauce</span>
  </h1>

  <p class="volume">175ml</p>

  <div class="barcode-space" aria-label="Space reserved for barcode"></div>

  <div class="product-notes">
    <p><strong>Shake well before use.</strong> Keep refrigerated after opening. &nbsp; <strong>Best before:</strong> ____ / ____ / ______</p>
    <p>Copper Lantern Sauce Co., 14 Ember Lane, Ashford SA 5035 · Australian made using 100% local ingredients</p>
  </div>

  <p class="origin-claim">MADE USING 100% FRESH<br>AUSTRALIAN PRODUCE</p>

  <div class="batch">
    <div class="write-in"></div>
    <span class="batch-label">BATCH No.</span>
  </div>
</main>
</body>
</html>
```